Vision / Mission Poster Required

We are looking to display our company Vision / Mission / Values on a poster. This will be displayed in the head office and other site offices.

The document needs to look professional however still be fun, eye catching and easy to read. It will be predominantly displayed in A3 format.

The design needs to use our company Logo which is attached along with the Text to display on the poster. I have put some additional text on the doc that you can include if it suits the layout but is not essential.

Target Market(s)

Staff, Corporate Visitors

Industry/Entity Type

Electric Company

Font styles to use
Sans Serif

Colors

Designer to choose colors to be used in the design.

Requirements
Must have
• Incorporate Logo
• Professional Look
• Attention grabbing
• Easy to Read
Should not have
• Lightning Bolts
• Pictures of random people/Things

```html
<!DOCTYPE html>
<html lang="en">
<head>
<meta charset="utf-8">
<title>Vantage Electrical – Vision, Mission and Values</title>
<link rel="stylesheet" href="https://fonts.googleapis.com/css2?family=Open+Sans:ital,wght@0,400;0,600;0,700;1,400&display=swap">
<style>
  :root {
    --navy: #1f3a70;
    --orange: #f26a21;
    --ink: #2b2b2b;
    --page: #ffffff;
    --backdrop: #e6e6e6;
  }
  * { box-sizing: border-box; margin: 0; padding: 0; }
  html, body { width: 931px; height: 1200px; overflow: hidden; }
  body {
    background: var(--backdrop);
    font-family: "Open Sans", Arial, sans-serif;
    color: var(--ink);
    position: relative;
  }
  .poster {
    position: absolute;
    left: 55px; top: 20px;
    width: 820px; height: 1160px;
    background: var(--page);
    overflow: hidden;
  }
  .masthead { position: relative; height: 78px; }
  .masthead svg { position: absolute; inset: 0; }
  .brand {
    position: absolute; left: 28px; top: 24px;
    display: flex; align-items: center; gap: 10px;
    color: var(--navy); font-weight: 700; font-size: 20px; letter-spacing: .3px;
    white-space: nowrap;
  }
  .brand-dot { width: 30px; height: 30px; border-radius: 50%; background: var(--orange); }
  .site-url {
    position: absolute; right: 26px; top: 25px;
    display: flex; align-items: center; gap: 8px;
    color: var(--orange); font-size: 19px;
  }
  .hero {
    height: 370px;
    background: linear-gradient(90deg, #2b2520 0%, #5e4a2c 22%, #d9a43a 42%, #e8bf4c 52%, #3a9fa8 70%, #e9a23b 88%, #f0b347 100%);
  }
  .content { padding: 18px 26px 0 27px; font-size: 14px; line-height: 1.36; }
  .section-title {
    display: inline-flex; align-items: stretch; height: 30px; margin-bottom: 6px;
  }
  .section-title span {
    background: var(--navy); color: var(--orange);
    font-weight: 700; font-size: 24px; line-height: 30px;
    padding: 0 22px 0 12px;
  }
  .section-title svg { display: block; }
  .vision p { margin-bottom: 2px; }
  .tagline { font-style: italic; }
  .mission { margin-top: 4px; }
  .mission ol { list-style: none; }
  .mission li { position: relative; padding-left: 35px; margin-bottom: 6px; }
  .step {
    position: absolute; left: 0; top: 2px;
    width: 24px; height: 24px; border-radius: 50%;
    background: var(--navy); color: #fff; border: 2px solid var(--orange);
    font-weight: 700; font-size: 13px; line-height: 20px; text-align: center;
  }
  .item-title { font-weight: 700; display: block; }
  .values { margin-top: 0; }
  .values ul { list-style: none; }
  .values li { position: relative; padding-left: 35px; margin-bottom: 2px; }
  .values li::before {
    content: ""; position: absolute; left: 14px; top: 8px;
    width: 6px; height: 6px; border-radius: 50%; background: var(--orange);
  }
  .footer-bar { position: absolute; left: 0; right: 0; bottom: 0; height: 10px; display: flex; }
  .footer-bar .navy { flex: 0 0 620px; background: var(--navy); }
  .footer-bar .orange { flex: 1; background: var(--orange); }
</style>
</head>
<body>
<main class="poster">
  <header class="masthead">
    <svg width="820" height="78" viewBox="0 0 820 78" aria-hidden="true">
      <polygon points="408,0 820,0 820,78 344,78" fill="var(--navy)"/>
      <polygon points="396,0 408,0 344,78 332,78" fill="var(--orange)"/>
    </svg>
    <div class="brand"><span class="brand-dot"></span>VANTAGE ELECTRICAL</div>
    <div class="site-url">
      <svg width="16" height="16" viewBox="0 0 16 16" aria-hidden="true">
        <g fill="none" stroke="var(--orange)" stroke-width="1.4">
          <circle cx="8" cy="8" r="6.5"/><ellipse cx="8" cy="8" rx="3" ry="6.5"/>
          <line x1="1.5" y1="8" x2="14.5" y2="8"/>
        </g>
      </svg>
      www.vantageelec.com.au
    </div>
  </header>

  <div class="hero" role="img" aria-label="Photograph of a modern shopping arcade with yellow hexagonal ceiling lights and a colourful mural wall"></div>

  <div class="content">
    <section class="vision">
      <h2 class="section-title"><span>Vision:</span><svg width="14" height="30" viewBox="0 0 14 30" aria-hidden="true"><polygon points="0,0 14,0 4,30 0,30" fill="var(--orange)"/></svg></h2>
      <p>To be Perth's premier provider of electrical service solutions</p>
      <p class="tagline">Optional Tag line: Dynamic results - Proven reputation</p>
    </section>

    <section class="mission">
      <h2 class="section-title"><span>Mission</span><svg width="14" height="30" viewBox="0 0 14 30" aria-hidden="true"><polygon points="0,0 14,0 4,30 0,30" fill="var(--orange)"/></svg></h2>
      <ol>
        <li><span class="step">1</span><span class="item-title">Deliver Growth and Value</span>By: - Maintaining a market presence - Leveraging our technical resources – Networking and developing stakeholder relationships</li>
        <li><span class="step">2</span><span class="item-title">Remain Profitable</span>By: - Increasing revenue – Optimizing capacity utilization – Maintaining expenses</li>
        <li><span class="step">3</span><span class="item-title">Be Sustainable</span>By: - Improving internal efficiency – Diversifying our income sources – Implementing Social &amp; Environmental improvement initiatives</li>
      </ol>
    </section>

    <section class="values">
      <h2 class="section-title"><span>Values:</span><svg width="14" height="30" viewBox="0 0 14 30" aria-hidden="true"><polygon points="0,0 14,0 4,30 0,30" fill="var(--orange)"/></svg></h2>
      <ul>
        <li><span class="item-title">Honesty &amp; Integrity</span>Customers, contractors and suppliers will be able to count on Vantage personnel to deal straightforwardly and adhere to the strictest moral and ethical codes of conduct.</li>
        <li><span class="item-title">Safety &amp; Responsibility</span>Vantage is committed to constantly improving safety practices at project job sites and within the electrical service industry as a whole.</li>
        <li><span class="item-title">Commitment to Quality</span>Customers and stakeholders will be able to count on Vantage's workmanship being among the best in the industry.</li>
        <li><span class="item-title">Innovation &amp; Technology</span>Customers can rely on us to apply the latest proven technologies on their projects, and to be on the ground floor of industry standards for new and emerging markets.</li>
        <li><span class="item-title">Knowledgeable &amp; Valued Employees</span>Vantage recognizes that its greatest asset is its people. We pledge to treat each employee with integrity, dealing honestly with all.</li>
      </ul>
    </section>
  </div>

  <div class="footer-bar"><span class="navy"></span><span class="orange"></span></div>
</main>
</body>
</html>
```